financial company web page

We are tax and financial consulting company that needs a web site. Our logo is attached. Headquarters of our company is based in Latvia, Riga. Our actual temporary web site is www.norquill.com The main purpose of our new web site is:
* to explain the benefits of doing business through Latvian LLC companies;
* provide necessary information about taxation regime in Latvia for trading and holding companies
* propose some standard schemes of using Latvian companies for various businesses.
* offer our clients other jurisdictions companies - other European, offshore, etc.
* offer our clients ecommerce solutions
* offer our client residency in Latvia and EU
Registration of a Latvian company + accounting + legal advice will be our primary product. However, web site first page should highlight 4 other important products, such as:
1 - eCommerce (here we will explain briefly what is eCommerce, how our client can use it, what are the bonuses doing business online, explain conditions of eCommerce, etc) ;
2 - Residence Permit (here we offer EU and non-EU citizens to obtain Latvian residence permit and explain the benefits of having Latvian ID card);
3 - other Jurisdictions (here we propose list of other companies registered in the countries with favorable taxation regime, i.e. UK, Hong-Kong, Canada, Panama, BVI, UAE, etc);
4 - banking (here we explain benefits of having bank account in Latvia, explaining briefly products that bank offer, etc).
Overall Website map is the following:
1. About us
2. About Latvia
3. Contacts
4. Latvian company
5. Our services
a. еCommerce
b. Resident permit (Latvia and EU)
c. Bank accounts
d. Registration and support of other jurisdictions (European companies, Low tax companies, Offshore companies)
e. Additional services (Tax advisory, Virtual office, European licenses, Accounting services, Legal address in Riga)
6. Become Partner
7. Tembrole Travel Guide
As a start point we need only first page design. If this design suits us well we will continue to work with you on other pages. We are looking for innovative, creative and professional design in line with our corporate logo and colours. We want this design to focus more on graphic, on simplicity and usability. It should be immediately clear from the first glance what the site is about, what is our key product and how to get more information if I'm interested on something.
These are website from our sector, we want to be better:
http://www.vantel-ridge.com/
http://www.qpr-harbourline.com/
http://www.dxlventurebuilders.com/
http://www.firmstarter318.co.uk/
In case you can't find our logo, please, ask I will send it to your mail. Thanks!
Target Market(s)
European, Russian or Chinesee enterpreneurs
Industry/Entity Type
Accounting
Requirements
Must have
- Web site will be on 10 languages, so somewhere must be a button/flag to switch language.
Contact information should be on every page (phone number and add Skype buttons or similar).
Search button should be available on the first page
Button Request a Call should be on every page.
Visitors should also have a possibility to download a brochure about each product (so appropriate button should be in each section).

```html
<!DOCTYPE html>
<html lang="en">
<head>
<meta charset="utf-8">
<title>Tembrole – Tax and Financial Solutions</title>
<link rel="stylesheet" href="https://fonts.googleapis.com/css2?family=Arimo:wght@400;700&family=Open+Sans:wght@400;600&display=swap">
<style>
:root{
  --navy:#062f6e;
  --navy-deep:#03215a;
  --brand-blue:#1d3f86;
  --link-blue:#1566b0;
  --pink:#d2115f;
  --pink-dark:#8e0b3b;
  --blue-card:#0a62b6;
  --blue-card-dark:#063d86;
  --green:#a7c90d;
  --green-dark:#5f7e08;
  --ink:#2b2b2b;
  --grey-text:#555;
  --line:#c8c8c8;
  --footer:#05105e;
}
*{box-sizing:border-box;margin:0;padding:0}
html,body{width:820px;height:1200px;overflow:hidden;background:#fff}
body{position:relative;font-family:"Arimo",Arial,sans-serif;color:var(--ink)}
.abs{position:absolute}

/* header */
.site-header{left:0;top:0;width:820px;height:81px;border-bottom:1px solid var(--navy-deep);background:#fff}
.brand{left:10px;top:6px;display:flex;align-items:center;gap:12px}
.brand-dot{width:52px;height:52px;border-radius:50%;background:var(--brand-blue)}
.brand-name{font-family:"Open Sans",sans-serif;font-weight:600;font-size:44px;color:var(--brand-blue);line-height:1;letter-spacing:-0.5px}
.brand-tagline{left:108px;top:54px;font-family:"Open Sans",sans-serif;font-size:10px;letter-spacing:1.2px;color:#7a8899}
.nav-home{left:310px;top:0;width:56px;height:95px;background:var(--pink);border-radius:0 0 4px 4px;color:#fff;font-family:"Open Sans",sans-serif;font-size:11px;text-align:center;padding-top:44px}
.nav{font-family:"Open Sans",sans-serif;font-size:11px;color:#555;white-space:nowrap}
.lang-switch{left:615px;top:10px;display:flex;gap:6px}
.lang-switch span{width:22px;height:22px;border-radius:50%;box-shadow:0 1px 2px rgba(0,0,0,.4)}

/* hero */
.hero{left:0;top:82px;width:820px;height:287px;background:radial-gradient(ellipse at 75% 40%,#1a5fae 0%,var(--navy) 45%,#042a63 100%)}
.hero-art{left:460px;top:82px;width:360px;height:287px;background:linear-gradient(160deg,rgba(70,150,220,.5) 0%,rgba(120,190,235,.45) 55%,rgba(200,170,60,.35) 100%)}
.hero-title{left:0;width:630px;top:150px;text-align:center;font-family:"Open Sans",sans-serif;color:#fff;font-size:24px;line-height:33px;letter-spacing:.3px}
.hero-title .accent{color:var(--pink);font-size:36px}
.btn{display:block;height:25px;border-radius:3px;background:linear-gradient(#fafafa,#c9c9c9);box-shadow:0 1px 2px rgba(0,0,0,.45);font-family:"Arimo",sans-serif;font-weight:700;font-size:12px;color:#333;text-align:center;line-height:25px;text-decoration:none}
.btn-hero{left:217px;top:254px;width:187px}
.btn .hl-pink{color:var(--pink)}
.btn .hl-blue{color:var(--link-blue)}
.btn .hl-green{color:#6b9a0a}

/* welcome */
.welcome-title{left:33px;top:400px;font-size:30px;font-weight:400;color:var(--ink)}
.welcome-lead{left:33px;top:451px;width:755px;font-size:13px;font-weight:700;line-height:16px;color:#111}
.welcome-body{left:33px;top:499px;width:760px;font-size:12.4px;line-height:15.7px;color:#333}
.learn-more{color:var(--pink);font-weight:700;font-size:13px;text-decoration:none;margin-left:14px}

/* service cards */
.card{top:596px;width:246px;height:276px;border-radius:4px;box-shadow:0 1px 3px rgba(0,0,0,.35);color:#fff}
.card-trading{left:30px;background:linear-gradient(#8c0b3d,#e0107e)}
.card-holding{left:284px;background:linear-gradient(#063c85,#1694dd)}
.card-ecom{left:538px;background:linear-gradient(#627f06,#cde20a)}
.card-title{position:absolute;left:0;width:100%;top:20px;text-align:center;font-family:"Open Sans",sans-serif;font-size:27px;text-shadow:0 1px 2px rgba(0,0,0,.4)}
.card-icon{position:absolute;left:64px;top:60px;width:100px;height:88px;border-radius:10px}
.card-text{position:absolute;left:22px;top:156px;width:210px;font-size:12.4px;line-height:15px}
.card .btn{position:absolute;left:31px;top:231px;width:187px}

/* info boxes */
.info{top:899px;width:246px;height:190px;border:1px solid var(--line);border-radius:4px;background:#fff}
.info-call{left:30px}
.info-contacts{left:284px}
.info-search{left:538px}
.info-title{position:absolute;left:21px;top:17px;font-family:"Open Sans",sans-serif;font-size:17px;color:var(--link-blue)}
.call-photo{position:absolute;left:0;top:52px;width:244px;height:130px;background:linear-gradient(90deg,#8ea7c0 0%,#c9d8e6 45%,#7f94a9 100%)}
.info-text{position:absolute;left:19px;font-size:12.4px;line-height:16px;color:#333}
.chat-btn{position:absolute;left:20px;top:130px;width:48px;height:48px;border-radius:50%;background:#12a6e6}
.search-field{position:absolute;left:19px;top:95px;width:208px;height:23px;border:1px solid #b5b5b5;background:#fff}
.btn-submit{position:absolute;left:19px;top:127px;width:75px;height:26px;line-height:26px}

/* footer */
.site-footer{left:0;top:1118px;width:820px;height:82px;background:radial-gradient(ellipse at 50% 60%,#0b2aa4 0%,var(--footer) 70%)}
.copyright{position:absolute;left:41px;top:34px;color:#fff;font-size:12.5px}
</style>
</head>
<body>

<header class="site-header abs">
  <div class="brand abs">
    <span class="brand-dot"></span>
    <span class="brand-name">Tembrole</span>
  </div>
  <div class="brand-tagline abs">TAX AND FINANCIAL SOLUTIONS</div>
</header>

<a class="nav-home abs">HOME</a>
<nav>
  <span class="nav abs" style="left:381px;top:44px">ABOUT US</span>
  <span class="nav abs" style="left:458px;top:44px">ABOUT LATVIA</span>
  <span class="nav abs" style="left:548px;top:44px">CONTACTS</span>
  <span class="nav abs" style="left:616px;top:44px">LATVIAN COMANY</span>
  <span class="nav abs" style="left:382px;top:64px">OUR SERVICES</span>
  <span class="nav abs" style="left:476px;top:64px">BECOME PARTNER</span>
  <span class="nav abs" style="left:589px;top:64px">TEMBROLE TRAVEL GUIDE</span>
</nav>

<div class="lang-switch abs" role="group" aria-label="Language selection">
  <span style="background:#23357a" aria-label="English"></span>
  <span style="background:#3a5bb0" aria-label="French"></span>
  <span style="background:#c52a1e" aria-label="German"></span>
  <span style="background:#d8231b" aria-label="Chinese"></span>
  <span style="background:#e6a21a" aria-label="Spanish"></span>
  <span style="background:#eeeeee" aria-label="Japanese"></span>
  <span style="background:#2f8a2f" aria-label="Portuguese"></span>
</div>

<section class="hero abs"></section>
<div class="hero-art abs" role="img" aria-label="Rising 3D bar chart with a golden growth arrow"></div>
<h1 class="hero-title abs"><span class="accent">LATVIA</span> IS YOUR PLATFORM FOR<br>INTERNATIONAL BUSINESS AND CAPITAL</h1>
<a class="btn btn-hero abs"><span class="hl-pink">CLICK HERE</span> FOR MORE</a>

<h2 class="welcome-title abs">Welcome Message</h2>
<p class="welcome-lead abs">Lorem ipsum dolor sit amet, consec tetuer adipiscing elit. Praesent vestibulum molestie lacus. Aenean nonummy hen drerit mauris. Phasellus porta. Fusce suscipit varius mi.</p>
<p class="welcome-body abs">Cum sociis natoque penatibus et magnis dis parturient montes, nascetur ridiculus mus. Nulla dui. Fusce feugiat malesuada odio. Morbi nunc odio, gravida at, cursus nec, luctus a, lorem. Maecenas tristique orci ac sem. Duis ultricies pharetra magna. D Donec sit amet eros. Lorem ipsum dolor sit amet, consectetuer adipiscing elit. Mauris fermentum dictum magna. Sed laoreet aliquam leo. Ut tellus dolor, dapibus eget, elementum vel, cursus eleifend, elit. Aenean auctor wisi et urna. <a class="learn-more">» Learn More</a></p>

<article class="card card-trading abs">
  <h3 class="card-title">Trading</h3>
  <div class="card-icon" role="img" aria-label="Yellow folder with a globe" style="background:linear-gradient(#f6e27a,#3b8ee0)"></div>
  <p class="card-text">Lorem ipsum dolor sit amet, consec tetuer adipiscing elit. Praesent ves tibulum molestie lacus.</p>
  <a class="btn"><span class="hl-pink">CLICK HERE</span> FOR MORE</a>
</article>

<article class="card card-holding abs">
  <h3 class="card-title">Holding</h3>
  <div class="card-icon" role="img" aria-label="Grey folder with a blue briefcase" style="background:linear-gradient(#e8ecf0,#3a86d0)"></div>
  <p class="card-text">Lorem ipsum dolor sit amet, consec tetuer adipiscing elit. Praesent ves tibulum molestie lacus.</p>
  <a class="btn"><span class="hl-blue">CLICK HERE</span> FOR MORE</a>
</article>

<article class="card card-ecom abs">
  <h3 class="card-title">E-commerce</h3>
  <div class="card-icon" role="img" aria-label="Green folder with a blue check mark" style="background:linear-gradient(#d9f27a,#2a7ed0)"></div>
  <p class="card-text">Lorem ipsum dolor sit amet, consec tetuer adipiscing elit. Praesent ves tibulum molestie lacus.</p>
  <a class="btn"><span class="hl-green">CLICK HERE</span> FOR MORE</a>
</article>

<section class="info info-call abs">
  <h4 class="info-title">REQUEST A CALL</h4>
  <div class="call-photo" role="img" aria-label="Photo of a smiling consultant on the phone in an office"></div>
</section>

<section class="info info-contacts abs">
  <h4 class="info-title">CONTACTS</h4>
  <p class="info-text" style="top:53px">Adress:Lindenmark street 12-7,<br>Riga, LV-1042, Latvia</p>
  <p class="info-text" style="top:101px">Phone number: + 371 20455108</p>
  <span class="chat-btn" aria-label="Online chat"></span>
</section>

<section class="info info-search abs">
  <h4 class="info-title">SEARCH</h4>
  <p class="info-text" style="top:53px">Lorem ipsum dolor sit amet, consec<br>tetuer adipiscing elit.</p>
  <input class="search-field" type="text" aria-label="Search">
  <a class="btn btn-submit">SUBMIT</a>
</section>

<footer class="site-footer abs">
  <p class="copyright">TEMBROLE COPYRGHT 2013</p>
</footer>

</body>
</html>
```